Serenelle Aura Candle Box Package Design

Two box sizes:
14oz Candle in a box Gift Boxes - 4 x 4 x 6
4oz Candle in a box Gift Boxes - 3 x 3 x 3
Website: www.serenelleaura.com
IG: @serenelle.aura
My brand is a sophisticated brand with luxury candles made of coconut wax.  Serenelle Aura means bright life. Our candles represent hope and light.
You matter, you are worthy, powerful and beautiful!
Each candle is hand poured, vegan, environmentally conscious, uniquely scented and rooted in the importance of self care and community. We donate a percentage of our proceeds to organizations that seek to empower and enrich women.
At Serenelle Aura, we believe that positive energy can move mountains.
We strive to elevate that energy in every way possible. Our candles are handmade with confident positivity in mind - 100% vegan friendly, non-toxic and carefully crafted for optimal performance yet minimal impact on the environment.

```html
<!DOCTYPE html>
<html lang="en">
<head>
<meta charset="utf-8">
<title>Serenelle Aura Candle Box</title>
<link rel="stylesheet" href="https://fonts.googleapis.com/css2?family=Archivo:wght@400;500;700;800&family=Arimo:wght@400&display=swap">
<style>
  :root {
    --page: #ffffff;
    --box-white: #f7f6f7;
    --lilac: #a78ba4;
    --mauve: #8f7489;
    --mauve-dark: #725a6e;
    --ink: #1e1c1e;
    --soft-ink: #4b4049;
    --plum-gold: #e4bf4a;
    --plum-deep: #6a4163;
    --edge: #dcd6db;
  }
  * { box-sizing: border-box; margin: 0; padding: 0; }
  html, body { width: 1200px; height: 1000px; overflow: hidden; }
  body {
    background: var(--page);
    font-family: "Archivo", Arial, sans-serif;
    color: var(--ink);
    position: relative;
  }
  .box-face {
    position: absolute;
    top: 190px;
    width: 340px;
    height: 340px;
    background: var(--box-white);
    border: 1px solid var(--edge);
    overflow: hidden;
  }
  .face-front { left: 60px; }
  .face-message { left: 430px; }
  .face-scents { left: 800px; }

  /* front face */
  .brand-name {
    position: absolute; top: 28px; left: 36px;
    font-weight: 800; font-size: 15px; letter-spacing: 0.3px;
  }
  .front-lilac-block {
    position: absolute; left: 150px; top: 70px;
    width: 150px; height: 150px; background: var(--lilac);
  }
  .plum-illustration {
    position: absolute; left: 110px; top: 56px;
    width: 150px; height: 160px;
    background: linear-gradient(120deg, var(--plum-gold) 0%, #dcae4c 50%, var(--plum-deep) 100%);
  }
  .front-info {
    position: absolute; left: 36px; right: 30px; bottom: 28px;
    display: flex; justify-content: space-between; align-items: flex-end;
    font-size: 8.5px; line-height: 1.15; text-transform: uppercase;
  }
  .front-info strong { font-weight: 800; display: block; }
  .net-weight .oz { font-weight: 800; font-size: 22px; line-height: 1; }
  .net-weight .oz small { font-size: 10px; }
  .net-weight .grams { font-size: 8px; text-transform: none; }

  /* message face */
  .affirmation-panel {
    position: absolute; left: 18px; top: 30px;
    width: 168px; height: 292px; background: var(--lilac);
    padding: 12px 10px;
    display: flex; flex-direction: column; justify-content: space-between;
    color: rgba(255,255,255,0.88);
    font-weight: 500; font-size: 19px; line-height: 1;
  }
  .affirmation-panel span { display: block; text-align: justify; text-align-last: justify; }
  .product-type {
    position: absolute; left: 190px; bottom: 14px;
    writing-mode: vertical-rl; transform: rotate(180deg);
    font-weight: 800; font-size: 27px; line-height: 1;
  }
  .product-title {
    position: absolute; right: 14px; top: 8px;
    font-weight: 800; font-size: 21px;
  }
  .mission-column {
    position: absolute; left: 222px; top: 38px;
    width: 50px; height: 284px; background: var(--mauve);
    padding: 6px 4px; color: #fff;
    font-weight: 700; font-size: 6.6px; line-height: 1.25;
  }
  .details {
    position: absolute; left: 278px; top: 38px; width: 56px;
    font-size: 4.3px; line-height: 1.3; color: var(--soft-ink);
  }
  .details p { margin-bottom: 5px; }
  .details .care-title { font-weight: 700; font-size: 5px; letter-spacing: 0.3px; }
  .details ul { list-style: none; }
  .details li::before { content: "• "; }
  .contact { margin-top: 8px; font-size: 4.6px; }
  .social-handle { display: flex; align-items: center; gap: 2px; margin-top: 2px; }
  .social-handle i { width: 4px; height: 4px; background: var(--soft-ink); display: inline-block; }

  /* scents face */
  .scents-band {
    position: absolute; left: 0; top: 20px; width: 100%; height: 50px;
    background: var(--mauve-dark);
  }
  .scent-list {
    position: absolute; left: 36px; top: 86px;
    writing-mode: vertical-lr;
    font-weight: 700; font-size: 7px; letter-spacing: 0.3px; line-height: 1.5;
    text-transform: uppercase; white-space: nowrap;
  }

  .presentation-note {
    position: absolute; left: 74px; top: 728px;
    font-family: "Arimo", Arial, sans-serif;
    font-size: 57px; font-weight: 400; color: var(--ink);
  }
</style>
</head>
<body>

<section class="box-face face-front">
  <div class="brand-name">serenelle aura</div>
  <div class="front-lilac-block"></div>
  <div class="plum-illustration" role="img" aria-label="Illustration of a halved plum with a green leaf"></div>
  <div class="front-info">
    <div><strong>Handmade<br>Candles</strong>With purpose<br>and love</div>
    <div><strong>Radiant<br>Plum</strong></div>
    <div class="net-weight"><div class="oz">14<small>OZ</small></div><div class="grams">396g</div></div>
  </div>
</section>

<section class="box-face face-message">
  <div class="affirmation-panel">
    <span>YOU MATTER,</span>
    <span>Y O U R</span>
    <span>WORTHY,</span>
    <span>BEAUTIFUL</span>
    <span>A N D</span>
    <span>POWERFUL</span>
  </div>
  <div class="product-type">luxury coconut</div>
  <div class="product-title">wax candle</div>
  <div class="mission-column">At Serenelle Aura, we believe that positive energy can move mountains.</div>
  <div class="details">
    <p>Our coconut wax candles are hand poured in small batches with clean fragrance and a cotton wick.</p>
    <p>We believe that self care and community light the way for every woman we serve.</p>
    <p>CLEAN | PARABEN FREE | VEGAN | PET FRIENDLY</p>
    <p>Trim the wick before each burn and let the wax melt evenly to the edges.</p>
    <p class="care-title">CANDLE CARE</p>
    <ul>
      <li>Burn for two to four hours at a time.</li>
      <li>Keep away from drafts and children.</li>
      <li>Never leave a burning candle alone.</li>
    </ul>
    <div class="contact">
      <div>www.serenelleaura.com</div>
      <div class="social-handle"><i></i>@serenelle.aura</div>
    </div>
  </div>
</section>

<section class="box-face face-scents">
  <div class="scents-band"></div>
  <div class="scent-list">Sweet fig | Bourbon | Plum | Patchouli |<br>Caramel | Honey | Cedar bark</div>
</section>

<div class="presentation-note">*MOCKUP FOR PRESENTATION ONLY</div>

</body>
</html>
```